Assessment Report cover design and formatting

This report is for senior executives and provides leaders with detailed insight into their capabilities and skills. The cover should have space for the date and name of the person doing the assessment. We are looking to modernise the report cover design. We would like the report to be our company colours if possible. The work will likely expand once the cover is done to other parts of the report, ie. the format and layout of the report etc.

Company colours:
Primary colours:
• Blue #0D47A1, #115CD0, #90B6ED, #EEf3FB
• Green #0D91A1, #47A10D, #324C196, #0DA11D
Additional colours:
• Purple #A10D91
• Brown #A1670D
• Red #A10D47

Target Market(s)

Executives

Industry/Entity Type

Consulting, leadership development

Colors
0094D4
00A9DD
6FCCEA
C7EBF8
E9F6FB
00AB8E
00BBA5
67D7C9
C6EFE9
E9F9F6
E54698
E96AAD
F1A4CE
F9D9EA
FCEFF6
6B429C
8869AF
B7A5CE
E3DAEB
F3F0F8

Requirements
Must have
• The report cover should have space for name of user, the date and company logo. Cover should be in A4 size.

```html
<!DOCTYPE html>
<html lang="en">
<head>
<meta charset="utf-8">
<title>Senior Leader Assessment – Insight Report</title>
<link href="https://fonts.googleapis.com/css2?family=Jost:wght@300;400;500&display=swap" rel="stylesheet">
<style>
  :root {
    --brand-blue: #0094D4;
    --ink: #1f1f1f;
    --muted: #6b6b6b;
    --rule: #bdbdbd;
    --navy: #2e2a7c;
    --paper: #ffffff;
  }
  html, body {
    margin: 0;
    padding: 0;
    overflow: hidden;
    background: var(--paper);
  }
  .cover {
    position: relative;
    width: 850px;
    height: 1200px;
    overflow: hidden;
    background: var(--paper);
    font-family: "Jost", "Futura", sans-serif;
    color: var(--ink);
  }
  .top-rule {
    position: absolute;
    left: 342px;
    top: 0;
    width: 3px;
    height: 226px;
    background: var(--rule);
  }
  .title {
    position: absolute;
    right: 92px;
    top: 228px;
    margin: 0;
    text-align: right;
    color: var(--brand-blue);
    font-weight: 400;
  }
  .title-main {
    display: block;
    font-size: 51px;
    line-height: 1;
    letter-spacing: 0.5px;
  }
  .title-sub {
    display: block;
    font-size: 30px;
    line-height: 1;
    margin-top: 8px;
  }
  .recipient-rule {
    position: absolute;
    left: 0;
    top: 364px;
    width: 66px;
    height: 3px;
    background: var(--rule);
  }
  .recipient {
    position: absolute;
    left: 78px;
    top: 357px;
  }
  .recipient-label {
    margin: 0;
    font-size: 15px;
    font-weight: 400;
    color: var(--muted);
    letter-spacing: 0.3px;
  }
  .recipient-name {
    margin: 26px 0 0;
    font-size: 31px;
    font-weight: 400;
    line-height: 1;
  }
  .recipient-date {
    margin: 16px 0 0;
    font-size: 18px;
    font-weight: 400;
  }
  .hero-art {
    position: absolute;
    left: 340px;
    top: 332px;
    width: 415px;
    height: 568px;
    background:
      linear-gradient(160deg, #4a4a50 0%, #4a4a50 14%, transparent 24%),
      linear-gradient(200deg, #e8503a 0%, transparent 22%),
      linear-gradient(150deg, #1fb8d6 20%, #7a5bd0 45%, #f2b21c 70%, #e98a1a 100%);
  }
  .accent-art {
    position: absolute;
    left: 594px;
    top: 838px;
    width: 178px;
    height: 176px;
    background: linear-gradient(135deg, #8e86d8 0%, #3fc6d6 45%, #f29a1c 100%);
    border-radius: 18px;
  }
  .brand {
    position: absolute;
    left: 338px;
    top: 946px;
  }
  .brand-name {
    font-size: 30px;
    font-weight: 400;
    color: var(--navy);
    letter-spacing: 0.5px;
    line-height: 1;
  }
  .classification {
    position: absolute;
    left: 338px;
    top: 1061px;
    display: flex;
    align-items: center;
    gap: 10px;
  }
  .classification-label {
    font-size: 19px;
    font-weight: 500;
    color: var(--brand-blue);
    letter-spacing: 0.3px;
  }
  .classification-rule {
    width: 358px;
    height: 3px;
    background: var(--rule);
  }
</style>
</head>
<body>
  <main class="cover">
    <div class="top-rule"></div>

    <h1 class="title">
      <span class="title-main">SENIOR LEADER</span>
      <span class="title-sub">ASSESSMENT</span>
    </h1>

    <div class="recipient-rule"></div>
    <section class="recipient">
      <p class="recipient-label">INSIGHT REPORT FOR:</p>
      <p class="recipient-name">Sample</p>
      <p class="recipient-date">22 August 2023</p>
    </section>

    <div class="hero-art" role="img" aria-label="Photograph of scattered colourful jigsaw puzzle pieces in purple, teal, orange and grey"></div>
    <div class="accent-art" role="img" aria-label="Three interlocking jigsaw pieces in lilac, teal and orange"></div>

    <div class="brand">
      <span class="brand-name">Keystone Advisory</span>
    </div>

    <div class="classification">
      <span class="classification-label">CONFIDENTIAL</span>
      <span class="classification-rule"></span>
    </div>
  </main>
</body>
</html>
```